Need a design for Loan Site with new age design

We need a design for our site www.fernpivot.in , we deal with different verticals like home loan, personal loan, loan against property and business loans. Feel free to get in touch if you have any questions.

I have like the concept of the drop down on the eye level where consumer is able to select the product they wish and continue with the form https://www.tallowcrest.com/ . They are in the same line of business as we are.

Here are few more designs which i personally like just to get idea about the taste

https://plumweatherly.com/
http://vexlar.com/partners

Industry/Entity Type

Loan

Number of Pages Required

2 page

Colors
34a7d7
add136
faa54b
fbee3e

Requirements
Must have
• I have like the concept of the drop down on the eye level where consumer is able to select the product they wish and continue with the form https://www.tallowcrest.com/ . They are in the same line of business as we are.
• Here are few more designs which i personally like just to get idea about the taste
• https://plumweatherly.com/
• http://vexlar.com/partners

```html
<!DOCTYPE html>
<html lang="en">
<head>
<meta charset="utf-8">
<title>Fern Pivot – Loans</title>
<link rel="stylesheet" href="https://fonts.googleapis.com/css2?family=Roboto:wght@300;400;500&family=Open+Sans:ital,wght@0,400;0,600;1,400&display=swap">
<style>
:root{
  --blue:#34a7d7;
  --blue-light:#4ec3ef;
  --green:#add136;
  --orange:#faa54b;
  --yellow:#fbee3e;
  --gold:#f2b51c;
  --ink:#444;
  --muted:#666;
  --band:#ebebeb;
  --footer:#474747;
}
*{box-sizing:border-box;margin:0;padding:0}
html,body{width:1200px;height:2184px;overflow:hidden;background:#fff}
body{font-family:"Open Sans",Arial,sans-serif;color:var(--ink);position:relative}
.abs{position:absolute}

/* header */
.site-header{position:absolute;left:0;top:0;width:1200px;height:131px;background:#fff;border-top:3px solid var(--blue)}
.brand{position:absolute;left:131px;top:44px;display:flex;align-items:center;gap:10px;font-family:"Roboto",sans-serif;font-weight:500;font-size:22px;color:var(--blue)}
.brand-mark{width:26px;height:26px;background:var(--blue)}
.main-nav{position:absolute;top:0;left:0;width:1200px;height:128px}
.main-nav a{position:absolute;top:62px;font-family:"Roboto",sans-serif;font-size:12px;color:#333;text-decoration:none;letter-spacing:.2px}
.main-nav a.active{color:var(--blue)}
.nav-underline{position:absolute;left:568px;top:124px;width:46px;height:4px;background:var(--blue)}

/* hero */
.hero{position:absolute;left:0;top:131px;width:1200px;height:432px;overflow:hidden}
.hero-photo{position:absolute;inset:0;background:linear-gradient(100deg,#6f7f90 0%,#9aa8b5 30%,#b9c4cc 55%,#a9b6c0 80%,#8a98a6 100%)}
.hero-shade{position:absolute;inset:0;background:rgba(40,55,70,.28)}
.hero h1{position:absolute;top:104px;width:1200px;text-align:center;font-family:"Roboto",sans-serif;font-weight:400;font-size:33px;color:#fff;letter-spacing:.3px}
.hero .tagline{position:absolute;top:171px;width:1200px;text-align:center;font-family:"Roboto",sans-serif;font-size:19px;color:#fff}
.loan-finder{position:absolute;left:332px;top:231px;height:47px;display:flex}
.loan-select{height:47px;background:#fff;font-size:11px;color:#555;padding:0 16px;display:flex;align-items:center;justify-content:space-between;border-right:1px solid #ddd}
.loan-select svg{width:9px;height:6px}
.sel-need{width:197px}
.sel-product{width:218px}
.search-btn{width:122px;height:47px;background:var(--blue-light);color:#fff;font-size:12px;display:flex;align-items:center;justify-content:center}

/* partners */
.partners{position:absolute;left:0;top:563px;width:1200px;height:111px;background:var(--band);display:flex;align-items:center;justify-content:center;gap:38px;box-shadow:inset 0 -3px 4px rgba(0,0,0,.05)}
.partner-badge{height:26px;background:#c9c9c9;border-radius:3px}

/* services */
.services{position:absolute;left:0;top:674px;width:1200px;height:367px;background:#fff}
.service{position:absolute;top:43px;width:270px;text-align:center}
.service-icon{width:105px;height:105px;border-radius:50%;margin:0 auto;display:flex;align-items:center;justify-content:center}
.service-icon svg{width:34px;height:34px}
.service h2{margin-top:36px;font-family:"Roboto",sans-serif;font-weight:400;font-size:19px;color:#444}
.service p{margin:18px auto 0;width:258px;font-size:11.5px;line-height:19px;color:#555}
.read-more{display:block;margin-top:15px;font-size:11.5px;color:#444}

/* features */
.features{position:absolute;left:0;top:1041px;width:1200px;height:466px;background:radial-gradient(ellipse at 55% 45%,#fafafa 0%,#ececec 60%,#e2e2e2 100%)}
.features-art{position:absolute;left:146px;top:66px;width:400px;height:313px;border-radius:6px;background:linear-gradient(135deg,#4a3f38 0%,#6b5c52 35%,#d9dde0 55%,#f1a54b 75%,#e7563a 100%);opacity:.85}
.features h2{position:absolute;left:609px;top:66px;font-family:"Roboto",sans-serif;font-weight:400;font-size:23px;color:var(--blue)}
.feature-list{position:absolute;left:603px;top:146px;list-style:none}
.feature-list li{display:flex;align-items:center;height:32px;margin-bottom:19px;font-size:14.5px;color:#444}
.feature-list li:nth-child(3){margin-bottom:15px}
.feature-icon{width:32px;height:32px;border-radius:50%;background:var(--blue);display:flex;align-items:center;justify-content:center;margin-right:17px}
.feature-icon svg{width:16px;height:16px}

/* testimonials */
.testimonials{position:absolute;left:0;top:1507px;width:1200px;height:390px;background:#fff}
.testimonials h2{position:absolute;top:48px;width:1200px;text-align:center;font-family:"Roboto",sans-serif;font-weight:400;font-size:23px;color:var(--blue)}
.quote{position:absolute;top:119px;width:291px}
.quote-box{position:relative;height:147px;background:#efefef;padding:20px 16px;font-size:11px;line-height:19px;color:#777;text-align:justify;text-align-last:center}
.quote-box::after{content:"";position:absolute;left:218px;bottom:-20px;border-left:0 solid transparent;border-right:20px solid transparent;border-top:20px solid #efefef}
.quote-author{position:absolute;left:190px;top:197px;font-style:italic;font-size:12px;color:#888}
.stars{position:absolute;left:197px;top:218px;display:flex;gap:1px}
.stars svg{width:10px;height:10px}

/* call to action */
.cta{position:absolute;left:0;top:1897px;width:1200px;height:144px;background:linear-gradient(180deg,#55c6f2 0%,#3aaee0 100%)}
.cta h2{position:absolute;top:34px;width:1200px;text-align:center;font-family:"Roboto",sans-serif;font-weight:400;font-size:23px;color:#fff}
.cta-btn{position:absolute;left:534px;top:76px;width:133px;height:38px;background:linear-gradient(180deg,#f7c936,#e9aa16);border-radius:2px;color:#fff;font-size:13px;display:flex;align-items:center;justify-content:center;letter-spacing:.3px}

/* footer */
.site-footer{position:absolute;left:0;top:2041px;width:1200px;height:143px;background:var(--footer);color:#fff;text-align:center}
.footer-nav{position:absolute;top:31px;width:1200px;font-size:10px;letter-spacing:.2px}
.footer-nav span{margin:0 4px}
.social{position:absolute;top:66px;width:1200px;display:flex;justify-content:center;gap:19px}
.social i{width:15px;height:15px;border-radius:50%;background:#fff;display:block}
.copyright{position:absolute;top:104px;width:1200px;font-size:9px;letter-spacing:.2px}
</style>
</head>
<body>

<header class="site-header">
  <div class="brand"><span class="brand-mark"></span>Fern Pivot</div>
  <nav class="main-nav">
    <a class="active" style="left:576px">HOME</a>
    <a style="left:655px">WHO WE ARE</a>
    <a style="left:766px">SERVICES</a>
    <a style="left:858px">BLOG</a>
    <a style="left:930px">CAREER</a>
    <a style="left:1016px">REACH US</a>
    <span class="nav-underline"></span>
  </nav>
</header>

<section class="hero">
  <div class="hero-photo" role="img" aria-label="Photo of a person in a striped shirt signing a loan document with a pen"></div>
  <div class="hero-shade"></div>
  <h1>LOOKING FOR A SECURED OR UNSECURED LOAN ?</h1>
  <p class="tagline">WE WILL HELP YOU GET BEST INTEREST RATE</p>
  <div class="loan-finder">
    <div class="loan-select sel-need">I would like to <svg viewBox="0 0 9 6"><path d="M1 1l3.5 3.5L8 1" fill="none" stroke="#666" stroke-width="1.3"/></svg></div>
    <div class="loan-select sel-product">Select Product <svg viewBox="0 0 9 6"><path d="M1 1l3.5 3.5L8 1" fill="none" stroke="#666" stroke-width="1.3"/></svg></div>
    <div class="search-btn">Search</div>
  </div>
</section>

<section class="partners" aria-label="Partner lenders">
  <span class="partner-badge" style="width:104px"></span>
  <span class="partner-badge" style="width:122px"></span>
  <span class="partner-badge" style="width:132px;height:56px"></span>
  <span class="partner-badge" style="width:114px"></span>
  <span class="partner-badge" style="width:142px"></span>
  <span class="partner-badge" style="width:122px"></span>
</section>

<section class="services">
  <article class="service" style="left:123px">
    <div class="service-icon" style="background:var(--green)">
      <svg viewBox="0 0 24 24"><path d="M12 3L2 12h3v8h5v-5h4v5h5v-8h3z" fill="#fff"/></svg>
    </div>
    <h2>HOME LOAN</h2>
    <p>Nemo enim ipsam voluptatem quia voluptas sit aspernatur aut odit aut fugit, sed quia consequuntur magni dolores</p>
    <span class="read-more">Read More »</span>
  </article>
  <article class="service" style="left:465px">
    <div class="service-icon" style="background:var(--orange)">
      <svg viewBox="0 0 24 24"><circle cx="12" cy="8" r="4.5" fill="#fff"/><path d="M3.5 21c0-5 3.8-7.5 8.5-7.5s8.5 2.5 8.5 7.5z" fill="#fff"/></svg>
    </div>
    <h2>PERSONAL LOAN</h2>
    <p>Nemo enim ipsam voluptatem quia voluptas sit aspernatur aut odit aut fugit, sed quia consequuntur magni dolores</p>
    <span class="read-more">Read More »</span>
  </article>
  <article class="service" style="left:806px">
    <div class="service-icon" style="background:var(--yellow)">
      <svg viewBox="0 0 24 24"><path d="M9 6V4h6v2" fill="none" stroke="#fff" stroke-width="2"/><rect x="2" y="6" width="20" height="14" rx="1.5" fill="#fff"/><rect x="10.5" y="11" width="3" height="3" fill="#fbee3e"/></svg>
    </div>
    <h2>BUSINESS LOAN</h2>
    <p>Nemo enim ipsam voluptatem quia voluptas sit aspernatur aut odit aut fugit, sed quia consequuntur magni dolores</p>
    <span class="read-more">Read More »</span>
  </article>
</section>

<section class="features">
  <div class="features-art" role="img" aria-label="Illustration of a cartoon businessman presenting a bar chart on a computer monitor"></div>
  <h2>OUR FEATURES</h2>
  <ul class="feature-list">
    <li><span class="feature-icon"><svg viewBox="0 0 16 16"><rect x="2" y="3" width="10" height="11" fill="none" stroke="#fff" stroke-width="1.5"/><path d="M7 10l7-7" stroke="#fff" stroke-width="1.8"/></svg></span>Get Approval within 7 business days</li>
    <li><span class="feature-icon"><svg viewBox="0 0 16 16"><circle cx="6.5" cy="6.5" r="4.3" fill="none" stroke="#fff" stroke-width="1.8"/><path d="M9.8 9.8L14 14" stroke="#fff" stroke-width="2"/></svg></span>Compare Quote from all major financial institutions</li>
    <li><span class="feature-icon"><svg viewBox="0 0 16 16"><path d="M1 7.5L15 1l-4 14-3-5.5z" fill="#fff"/></svg></span>Doorstep Deliveries</li>
    <li><span class="feature-icon"><svg viewBox="0 0 16 16"><path d="M8 1L1 5h14z" fill="#fff"/><rect x="3" y="6" width="2" height="6" fill="#fff"/><rect x="7" y="6" width="2" height="6" fill="#fff"/><rect x="11" y="6" width="2" height="6" fill="#fff"/><rect x="1" y="13" width="14" height="2" fill="#fff"/></svg></span>Easy Documentation</li>
  </ul>
</section>

<section class="testimonials">
  <h2>TESTIMONIALS</h2>
  <figure class="quote" style="left:131px">
    <blockquote class="quote-box">"Lorem ipsum dolor sit amet, consectetur adipiscing elit, sed do eiusmod tempor incididunt ut labore et dolore magna aliqua. Ut enim ad minim veniam, quis nostrud exercitation ullamco laboris nisi ut aliquip "</blockquote>
    <figcaption class="quote-author">- John Doe -</figcaption>
    <div class="stars"><svg viewBox="0 0 10 10"><path d="M5 0l1.5 3.3 3.5.3-2.7 2.3.8 3.6L5 7.6 1.9 9.5l.8-3.6L0 3.6l3.5-.3z" fill="#e8b514"/></svg><svg viewBox="0 0 10 10"><path d="M5 0l1.5 3.3 3.5.3-2.7 2.3.8 3.6L5 7.6 1.9 9.5l.8-3.6L0 3.6l3.5-.3z" fill="#e8b514"/></svg><svg viewBox="0 0 10 10"><path d="M5 0l1.5 3.3 3.5.3-2.7 2.3.8 3.6L5 7.6 1.9 9.5l.8-3.6L0 3.6l3.5-.3z" fill="#e8b514"/></svg><svg viewBox="0 0 10 10"><path d="M5 0l1.5 3.3 3.5.3-2.7 2.3.8 3.6L5 7.6 1.9 9.5l.8-3.6L0 3.6l3.5-.3z" fill="#e8b514"/></svg><svg viewBox="0 0 10 10"><path d="M5 0l1.5 3.3 3.5.3-2.7 2.3.8 3.6L5 7.6 1.9 9.5l.8-3.6L0 3.6l3.5-.3z" fill="#e8b514"/></svg></div>
  </figure>
  <figure class="quote" style="left:454px">
    <blockquote class="quote-box">"Lorem ipsum dolor sit amet, consectetur adipiscing elit, sed do eiusmod tempor incididunt ut labore et dolore magna aliqua. Ut enim ad minim veniam, quis nostrud exercitation ullamco laboris nisi ut aliquip "</blockquote>
    <figcaption class="quote-author">- John Doe -</figcaption>
    <div class="stars"><svg viewBox="0 0 10 10"><path d="M5 0l1.5 3.3 3.5.3-2.7 2.3.8 3.6L5 7.6 1.9 9.5l.8-3.6L0 3.6l3.5-.3z" fill="#e8b514"/></svg><svg viewBox="0 0 10 10"><path d="M5 0l1.5 3.3 3.5.3-2.7 2.3.8 3.6L5 7.6 1.9 9.5l.8-3.6L0 3.6l3.5-.3z" fill="#e8b514"/></svg><svg viewBox="0 0 10 10"><path d="M5 0l1.5 3.3 3.5.3-2.7 2.3.8 3.6L5 7.6 1.9 9.5l.8-3.6L0 3.6l3.5-.3z" fill="#e8b514"/></svg><svg viewBox="0 0 10 10"><path d="M5 0l1.5 3.3 3.5.3-2.7 2.3.8 3.6L5 7.6 1.9 9.5l.8-3.6L0 3.6l3.5-.3z" fill="#e8b514"/></svg><svg viewBox="0 0 10 10"><path d="M5 0l1.5 3.3 3.5.3-2.7 2.3.8 3.6L5 7.6 1.9 9.5l.8-3.6L0 3.6l3.5-.3z" fill="#e8b514"/></svg></div>
  </figure>
  <figure class="quote" style="left:776px">
    <blockquote class="quote-box">"Lorem ipsum dolor sit amet, consectetur adipiscing elit, sed do eiusmod tempor incididunt ut labore et dolore magna aliqua. Ut enim ad minim veniam, quis nostrud exercitation ullamco laboris nisi ut aliquip "</blockquote>
    <figcaption class="quote-author">- John Doe -</figcaption>
    <div class="stars"><svg viewBox="0 0 10 10"><path d="M5 0l1.5 3.3 3.5.3-2.7 2.3.8 3.6L5 7.6 1.9 9.5l.8-3.6L0 3.6l3.5-.3z" fill="#e8b514"/></svg><svg viewBox="0 0 10 10"><path d="M5 0l1.5 3.3 3.5.3-2.7 2.3.8 3.6L5 7.6 1.9 9.5l.8-3.6L0 3.6l3.5-.3z" fill="#e8b514"/></svg><svg viewBox="0 0 10 10"><path d="M5 0l1.5 3.3 3.5.3-2.7 2.3.8 3.6L5 7.6 1.9 9.5l.8-3.6L0 3.6l3.5-.3z" fill="#e8b514"/></svg><svg viewBox="0 0 10 10"><path d="M5 0l1.5 3.3 3.5.3-2.7 2.3.8 3.6L5 7.6 1.9 9.5l.8-3.6L0 3.6l3.5-.3z" fill="#e8b514"/></svg><svg viewBox="0 0 10 10"><path d="M5 0l1.5 3.3 3.5.3-2.7 2.3.8 3.6L5 7.6 1.9 9.5l.8-3.6L0 3.6l3.5-.3z" fill="#e8b514"/></svg></div>
  </figure>
</section>

<section class="cta">
  <h2>WHAT ARE YOU WAITING FOR?</h2>
  <span class="cta-btn">INQUIRE NOW</span>
</section>

<footer class="site-footer">
  <nav class="footer-nav">HOME<span>/</span>WHO WE ARE<span>/</span>SERVICES<span>/</span>BLOG<span>/</span>CAREER<span>/</span>REACH US</nav>
  <div class="social" aria-label="Social links"><i></i><i></i><i></i><i></i><i></i></div>
  <p class="copyright">COPYRIGHT © 2016 FERN PIVOT</p>
</footer>

</body>
</html>
```